Label Design for Food Brand

We want a modern label for our spice blends. We are completely open in which direction, it should be modern and beautiful.

Use for Sample spice mixture: "BBQ Tangio"

Here the Packaging:
https://www.kolm-tiegelhaus.example/media/xlarge/1700_1.jpg
Abmessung: Ø 54 x 67 mm

Food

Food

• Logo, Name of Tangio
• Images of food

```html
<!DOCTYPE html>
<html lang="en">
<head>
<meta charset="utf-8">
<title>BBQ Tangio – Spice Label</title>
<link rel="stylesheet" href="https://fonts.googleapis.com/css2?family=Jost:wght@300;400;600;700;800&display=swap">
<style>
  :root {
    --ink: #141414;
    --label-light: #f8f8f8;
    --label-shade: #e6e6e6;
    --page: #ffffff;
  }
  * { box-sizing: border-box; margin: 0; padding: 0; }
  html, body {
    width: 1200px;
    height: 750px;
    overflow: hidden;
    background: var(--page);
    font-family: "Jost", sans-serif;
    color: var(--ink);
  }
  .label {
    position: absolute;
    left: 150px;
    top: 95px;
    width: 900px;
    height: 560px;
    display: flex;
    background: linear-gradient(90deg, var(--label-shade) 0%, var(--label-light) 45%, var(--label-light) 70%, var(--label-shade) 100%);
  }
  .brand-strip {
    width: 130px;
    border-right: 5px solid var(--ink);
    position: relative;
  }
  .brand-name {
    position: absolute;
    left: 50%;
    bottom: 40px;
    transform-origin: left center;
    transform: rotate(-90deg) translateY(-50%);
    white-space: nowrap;
    font-size: 64px;
    font-weight: 600;
    letter-spacing: 1px;
    line-height: 1;
    translate: 0 0;
  }
  .product {
    flex: 1;
    padding: 40px 60px 40px 60px;
    display: flex;
    flex-direction: column;
  }
  .product-type {
    font-size: 215px;
    font-weight: 300;
    line-height: 0.85;
    letter-spacing: 2px;
  }
  .product-name {
    font-size: 150px;
    font-weight: 800;
    line-height: 0.95;
    letter-spacing: 1px;
    margin-top: 10px;
  }
  .tagline {
    margin-top: 22px;
    font-size: 33px;
    line-height: 1.05;
    font-weight: 300;
    letter-spacing: 1px;
  }
  .tagline strong { font-weight: 700; }
  .claims {
    margin-top: 18px;
    border-top: 4px solid var(--ink);
    display: grid;
    grid-template-columns: 1fr 1fr 1fr;
  }
  .claim {
    padding: 18px 0 14px;
    text-align: center;
    font-size: 24px;
    font-weight: 300;
    letter-spacing: 1px;
  }
  .claim + .claim { border-left: 4px solid var(--ink); }
  .claim strong { font-weight: 700; }
</style>
</head>
<body>
  <section class="label">
    <div class="brand-strip">
      <span class="brand-name">TANGIO FOOD</span>
    </div>
    <div class="product">
      <h1 class="product-type">BBQ</h1>
      <h2 class="product-name">TANGIO</h2>
      <p class="tagline">HANDCRAFTED WITH <strong>HIGHEST<br>QUALITY INGREDIENTS</strong></p>
      <div class="claims">
        <p class="claim">GLUTEN <strong>FREE</strong></p>
        <p class="claim">NO <strong>MSG</strong></p>
        <p class="claim">NO <strong>SOY</strong></p>
      </div>
    </div>
  </section>
</body>
</html>
```